Boat Dealership Needs A Post Boat Show Sale Flyer - 8.5X11

We need an 8.5X11 flyer to hand out at our boat show to promote a sale at our dealership following our boat show.

Annual Post Boat Show Open House

February 25 - March 5
Extended Hours
Friday, February 25 - 9 AM to 6 PM
Saturday, February 26 -9 AM to 6 PM
Sunday, February 27 - 11 AM to 3 PM
Monday, February 28 through Friday, March 4 - 9 AM to 6 PM
Saturday, March 5 - 9 AM to 3 PM
After hours by appointment

Phone - (555) 418-3627
Website – harbeldmarine.example

Didn't buy at the show? Wondering what to do after the show?
Don't miss your last chance to secure boat show season pricing.
Our three large, indoor showrooms are fully stocked, and our discounted boat show pricing continues.
Extended hours and continued show pricing.
In-stock incentives and special financing.
New pontoons in-stock starting at $25,995 and less than $150 a month with approved credit.
New tritoons in stock starting at $38,995 and less than $250 a month with approved credit.
Side console Talvin Hulls fishing boats starting at $17,995 and less than $125 a month with approved credit.
Special pricing on remaining in-stock Vorlanes.
Save thousands on Delsmoor.

Family-owned relaxed atmosphere.
Refreshments provided.
Prefer to shop virtually? Shop 24/7 on our website at harbeldmarine.example or set up a real-time video call.

Proudly Offering – Harbeld, Ketrin, Ondaway, and Drayloft Pontoons, Vorlane, Quilto, Delsmoor, Talvin Hulls

We would like our brand logos on the design.

Follow Us On Plazaly, Snapverse, and Vidloop

Colors
FFF300
FFF600
FEFA6F
FFFEC7
FFFEE8
FFC000
F8CF3A
FAE287
FDF2CF
FEFAEE
F0912C
F2A743
F7CA91
FBE8D2
FDF5EE
EE7325
F08F49
F5BC92
FAE3D3
FDF4ED
EB3D1F
EC4F4E
F09395
F8D3D4
FCEDEE

```html
<!DOCTYPE html>
<html lang="en">
<head>
<meta charset="utf-8">
<title>Annual Post Boat Show Open House – Harbeld</title>
<link href="https://fonts.googleapis.com/css2?family=Montserrat:wght@400;500;600;700;800;900&family=Oswald:wght@500;600&display=swap" rel="stylesheet">
<style>
:root{
  --red:#c8101a;
  --ink:#111111;
  --night:#0b0c10;
  --paper:#ffffff;
  --bg:#ececec;
  --grey:#d9d9d9;
  --line:#9a9a9a;
}
*{margin:0;padding:0;box-sizing:border-box}
html,body{width:748px;height:1200px;overflow:hidden;background:var(--bg)}
body{font-family:"Montserrat",sans-serif;color:var(--ink);position:relative}
.sheet{position:absolute;top:380px;width:340px;height:440px;overflow:hidden;box-shadow:0 6px 18px rgba(0,0,0,.25)}
.sheet--front{left:24px;background:linear-gradient(#ffffff 0%,#f1f1f1 36%,#1f2430 76%,#0b0c10 100%)}
.sheet--back{left:384px;background:var(--paper)}
.abs{position:absolute}
.center{left:0;right:0;text-align:center}
.hcenter{left:50%;transform:translateX(-50%);white-space:nowrap}

/* wordmark */
.brand{font-weight:800;letter-spacing:2px;color:var(--red);line-height:1}
.front-brand{top:18px;font-size:17px}
.back-brand{top:18px;font-size:14px;color:#fff}

/* front */
.title-annual{top:50px;font-weight:900;font-size:58px;line-height:1;color:var(--red);letter-spacing:-1px}
.title-post{top:110px;font-weight:800;font-size:25px;line-height:1;color:var(--red)}
.title-open{top:136px;font-weight:900;font-size:31px;line-height:1;color:var(--ink)}
.front-photo{left:0;top:176px;width:340px;height:140px;background:linear-gradient(#d5e0ee 0%,#a9bad2 40%,#5d6b84 75%,rgba(31,36,48,0) 100%)}
.date-band{background:var(--red);color:#fff;font-family:"Oswald",sans-serif;font-weight:600;font-size:20px;padding:2px 10px;line-height:1.2}
.date-band sup,.date-tab sup{font-size:.55em}
.front-date{top:306px}
.front-tag{top:346px;color:#fff;font-weight:700;font-size:12.5px;line-height:1.35}
.rule{height:1px;background:#555}
.front-rule{top:392px;left:30px;width:280px}

/* footer */
.footer{display:flex;align-items:center;justify-content:space-between;left:16px;right:16px}
.footer__phone{font-weight:600;font-size:11.5px;display:flex;align-items:center;gap:3px}
.footer__addr{font-size:5px;line-height:1.8}
.footer__addr span{display:flex;align-items:center;gap:3px}
.footer__follow{font-weight:600;font-size:8px;line-height:1.4}
.socials{display:flex;gap:3px}
.socials i{display:block;width:8px;height:8px;border-radius:50%;background:var(--red)}
.front-footer{top:404px;color:#fff}

/* back */
.back-header{left:0;top:0;width:340px;height:50px;background:linear-gradient(#2c2f36,#101216)}
.date-tab{top:38px;background:#fff;font-family:"Oswald",sans-serif;font-weight:500;font-size:15px;padding:0 6px;line-height:1.4}
.date-tab .r{color:var(--red)}
.hours-box{left:26px;top:70px;width:288px;height:84px;border:1px solid var(--line);border-radius:7px}
.label-red{background:var(--red);color:#fff;font-weight:600;line-height:1.35;border-radius:2px}
.hours-label{top:63px;font-size:9.5px;padding:0 6px}
.hours-list{top:80px;font-weight:700;font-size:5.6px;color:var(--red);line-height:11px}
.hours-list li{list-style:none;background:linear-gradient(90deg,transparent 15%,#e5e5e5 50%,transparent 85%) bottom/100% 1px no-repeat}
.after-hours{top:146px;background:#fff;padding:0 4px;font-weight:700;font-size:6.6px}
.promo-box{left:26px;top:160px;width:288px;height:55px;border:1px solid var(--line);border-radius:7px;overflow:hidden}
.promo-box__head{font-size:7.2px;text-align:center;border-radius:0}
.promo-list{display:grid;grid-template-columns:1fr 1fr;gap:6px 8px;padding:5px 8px;font-weight:600;font-size:4.3px;line-height:1.3}
.promo-list li{list-style:none;display:flex;gap:3px;align-items:flex-start}
.promo-list li::before{content:"";flex:none;width:4px;height:4px;border:0.8px solid var(--red);border-radius:50%}
.cards{left:26px;top:222px;width:288px;display:flex;gap:7px}
.card{flex:1;border:1px solid var(--line);border-radius:3px;height:80px;text-align:center;position:relative;overflow:hidden}
.card__head{background:var(--red);color:#fff;font-size:6.4px;line-height:1.15;height:16px;display:flex;align-items:center;justify-content:center;padding:0 3px}
.card__head--two{font-size:5.6px}
.card__small{font-size:5px;color:#333;margin-top:2px}
.card__price{font-size:15px;font-weight:500;line-height:1.1}
.card__tiny{font-size:3.8px;color:#555;line-height:1.1}
.card__month{font-size:7px;line-height:1}
.card__foot{position:absolute;left:3px;right:3px;bottom:3px;background:#1d1d1d;color:#fff;font-size:5px;line-height:9px;border-radius:2px}
.special{top:305px;font-size:6.4px;line-height:1.25}
.back-rule{top:323px;left:28px;width:284px;background:#e0a0a0}
.family{top:328px;font-weight:700;font-size:7.2px}
.virtual-label{top:345px;font-size:7.4px;padding:0 6px}
.virtual{top:358px;font-size:6px}
.virtual b{color:var(--red);font-weight:800}
.virtual b.big{font-size:10px}
.offering{left:26px;top:378px;width:288px;height:32px;display:flex;background:var(--grey)}
.offering__label{background:var(--ink);color:#fff;font-weight:700;font-size:8px;line-height:1.15;padding:0 6px;display:flex;align-items:center;width:58px}
.offering__brands{flex:1;display:grid;grid-template-columns:repeat(4,1fr);align-items:center;text-align:center;font-weight:700;font-size:5.6px;color:#333}
.back-footer{top:416px;color:var(--ink)}
.icon{width:6px;height:6px;fill:var(--red)}
</style>
</head>
<body>

<section class="sheet sheet--front" aria-label="Flyer front">
  <div class="abs center brand front-brand">HARBELD</div>
  <div class="abs front-photo" role="img" aria-label="Photo of people jumping off a wake boat on a lake under a blue sky"></div>
  <h1 class="abs center title-annual">ANNUAL</h1>
  <h2 class="abs center title-post">POST BOAT SHOW</h2>
  <h2 class="abs center title-open">OPEN HOUSE</h2>
  <div class="abs hcenter date-band front-date">25<sup>TH</sup> FEBRUARY TO 5<sup>TH</sup> MARCH</div>
  <p class="abs center front-tag">FAMILY-OWNED RELAXED ATMOSPHERE.<br>REFRESHMENTS PROVIDED.</p>
  <div class="abs rule front-rule"></div>
  <div class="abs footer front-footer">
    <div class="footer__phone"><svg class="icon" viewBox="0 0 10 10"><path d="M2 0l2 2.5-1 1.2c.6 1.3 1.6 2.3 2.9 2.9L7.1 5.6 10 7.6 8.8 9.6C4.5 9.6.4 5.5.4 1.2z"/></svg>(555) 418-3627</div>
    <div class="footer__addr">
      <span><svg class="icon" viewBox="0 0 10 10"><path d="M5 0a3.5 3.5 0 0 0-3.5 3.5C1.5 6 5 10 5 10s3.5-4 3.5-6.5A3.5 3.5 0 0 0 5 0zm0 5a1.5 1.5 0 1 1 0-3 1.5 1.5 0 0 1 0 3z"/></svg>4180 N. Calloway Rd Brennick, MI 49012</span>
      <span><svg class="icon" viewBox="0 0 10 10"><circle cx="5" cy="5" r="4.3" fill="none" stroke="#c8101a" stroke-width="1"/></svg>harbeldmarine.example</span>
    </div>
    <div class="footer__follow">Follow Us On<div class="socials"><i></i><i></i><i></i></div></div>
  </div>
</section>

<section class="sheet sheet--back" aria-label="Flyer back">
  <div class="abs back-header" role="img" aria-label="Darkened photo of a boat on the water"></div>
  <div class="abs center brand back-brand">HARBELD</div>
  <div class="abs hcenter date-tab"><span class="r">25<sup>TH</sup></span> FEBRUARY TO <span class="r">5<sup>TH</sup></span> MARCH</div>

  <div class="abs hours-box"></div>
  <div class="abs hcenter label-red hours-label">EXTENDED HOURS</div>
  <ul class="abs center hours-list">
    <li>Friday, February 25 - 9 AM to 6 PM</li>
    <li>Saturday, February 26 - 9 AM to 6 PM</li>
    <li>Sunday, February 27 - 11 AM to 3 PM</li>
    <li>Monday, February 28 through Friday, March 4 - 9 AM to 6 PM</li>
    <li>Saturday, March 5 - 9 AM to 3 PM</li>
  </ul>
  <div class="abs hcenter after-hours">AFTER HOURS BY APPOINTMENT</div>

  <div class="abs promo-box">
    <div class="label-red promo-box__head">Didn't buy at the show? Wondering what to do after the show?</div>
    <ul class="promo-list">
      <li>Don't miss your last chance to secure boat show season pricing.</li>
      <li>Our three large, indoor showrooms are fully stocked, and our discounted boat show pricing continues.</li>
      <li>Extended hours and continued show pricing.</li>
      <li>In-stock incentives and special financing</li>
    </ul>
  </div>

  <div class="abs cards">
    <div class="card">
      <div class="card__head">New pontoons in-stock</div>
      <div class="card__small">starting at</div>
      <div class="card__price">$25,995</div>
      <div class="card__tiny">and less than</div>
      <div class="card__month">$150</div>
      <div class="card__tiny">a month</div>
      <div class="card__foot">with approved credit.</div>
    </div>
    <div class="card">
      <div class="card__head">New tritoons in stock</div>
      <div class="card__small">starting at</div>
      <div class="card__price">$ 38,995</div>
      <div class="card__tiny">and less than</div>
      <div class="card__month">$250</div>
      <div class="card__tiny">a month</div>
      <div class="card__foot">with approved credit.</div>
    </div>
    <div class="card">
      <div class="card__head card__head--two">Side console Talvin Hulls<br>fishing boats</div>
      <div class="card__small">starting at</div>
      <div class="card__price">$ 17,995</div>
      <div class="card__tiny">and less than</div>
      <div class="card__month">$125</div>
      <div class="card__tiny">a month</div>
      <div class="card__foot">with approved credit.</div>
    </div>
  </div>

  <p class="abs center special">Special pricing on remaining in-stock Vorlanes.<br>Save thousands on Delsmoor.</p>
  <div class="abs rule back-rule"></div>
  <p class="abs center family">FAMILY-OWNED RELAXED ATMOSPHERE. REFRESHMENTS PROVIDED.</p>
  <div class="abs hcenter label-red virtual-label">Prefer to shop virtually?</div>
  <p class="abs center virtual">Shop <b class="big">24/7</b> on our website at <b>harbeldmarine.example</b> or set up a real-time video call.</p>

  <div class="abs offering">
    <div class="offering__label">PROUDLY OFFERING</div>
    <div class="offering__brands">
      <span>Harbeld</span><span>Drayloft</span><span>Delsmoor</span><span>Vorlanes</span>
      <span>Ondaway</span><span>Quilto</span><span>Talvin Hulls</span><span>Ketrin</span>
    </div>
  </div>

  <div class="abs footer back-footer">
    <div class="footer__phone"><svg class="icon" viewBox="0 0 10 10"><path d="M2 0l2 2.5-1 1.2c.6 1.3 1.6 2.3 2.9 2.9L7.1 5.6 10 7.6 8.8 9.6C4.5 9.6.4 5.5.4 1.2z"/></svg>(555) 418-3627</div>
    <div class="footer__addr">
      <span><svg class="icon" viewBox="0 0 10 10"><path d="M5 0a3.5 3.5 0 0 0-3.5 3.5C1.5 6 5 10 5 10s3.5-4 3.5-6.5A3.5 3.5 0 0 0 5 0zm0 5a1.5 1.5 0 1 1 0-3 1.5 1.5 0 0 1 0 3z"/></svg>4180 N. Calloway Rd Brennick, MI 49012</span>
      <span><svg class="icon" viewBox="0 0 10 10"><circle cx="5" cy="5" r="4.3" fill="none" stroke="#c8101a" stroke-width="1"/></svg>harbeldmarine.example</span>
    </div>
    <div class="footer__follow">Follow Us On<div class="socials"><i></i><i></i><i></i></div></div>
  </div>
</section>

</body>
</html>
```